2-Page Flyer for the Information Session about the Quiet Venture Pathway

This is a flyer to announce/advertise an evening Information Session about the Quiet Venture Pathway. This Program aims at mindfully rethinking and redesigning work (and life) for people who feel stuck or not entirely satisfied with their work and/or life (please see draft flyer attached for more details). This Program is property of Bright Meadow, a company that uses a combination of Mindfulness, Design, and Entrepreneurship to help people achieve greater happiness (in their work and lives).
Updates

Target Market(s)

People who feel stuck or not entirely satisfied with their work and/or life (please see draft flyer attached for more details)

Font styles to use
Serif
Sans Serif

Colors
ffffff
f37122
33a6d7
acd037

Requirements
Must have
• All of what I will say below is suggestive (I’m not a design expert), and I’m open to divert from it, if it makes sense and feels more interesting.
• I thought initially of a 2-page flyer (please see draft flyer attached). The first page could help people grasp the essence of the event quickly (in 1 or 2 minutes), and then, if they are interested/motivated, they would continue reading through page 2, which has more info about the Program in itself.
• Potential Structure
• Page 1
• . About the Information Session on the Quiet Venture Pathway
• . Visible Date & Time, Contacts, Venue (and other relevant info)
• . About me (the facilitator)
• Page 2
• . About the Quiet Venture Pathway
• I include a Powerpoint draft of the flyer with the content. The design is rudimentary and precarious from an aesthetics/organization point of view, and this is mainly where I need help (and maybe in other aspects too!).
• On the flyer, I would like to include:
• . A photo of myself (I attach 1 picture).
• . 1 or 2 beautiful-nature photos (cropped or full). One may have to do with looking at the sky, dreaming, and imagining a new work and life (2 photos with sky and clouds attached). The other has to do with walking the transformation journey (the photo with the person walking through the forest path).
• . bright meadow logo or logos (there are two slightly different ones, that can be used for different purposes). For the first page, I would like the bright meadow logo that has "bright meadow" written on the bottom, with the saying "Calm, Craft and Enterprise for Joyful Living" beneath. This is the main logo. For the 2nd page, you can choose the logo that adapts better.
• - Where it says the "the way out is in" it would be great to have a similar font to the one I attach (see file "Font_the_way_out_is_in.png" and Torvenscript-qr.ttf
Nice to have
• In terms of colours, I would not divert much from the logo colours (and of course white and black). I would like the flyer to be quite white. Almost like fairy-tale white: the white horse, the white snow, the white of the stars, the white heaven. White could be the base colour. White means peace, tranquillity, calm contentment, a smile.
• And then use the other colours. The green of the mindfulness. The blue of the sky, the dreams. And the orange of the sun, the energy, the fire, the action. And maybe the black for text.
• Where it says the "the way out is in" it would be great to have a similar font to the one I attach (see file "Font_the_way_out_is_in".
• I would like this flyer to be a piece of art, in every possible way. Simple, beautiful, ease, light, peaceful, calm happy. Just like the Quiet Venture Pathway and bright meadow Company that I am creating intends to be. The mission of this Program and Company is to be a designer, a painter (a Picasso) of happier and more fulfilling human lives.
• I am very much looking forward to seeing your proposal(s).

```html
<!DOCTYPE html>
<html lang="en">
<head>
<meta charset="utf-8">
<title>Quiet Venture Pathway – Information Session Flyer</title>
<link rel="stylesheet" href="https://fonts.googleapis.com/css2?family=Berkshire+Swash&family=Didact+Gothic&family=Montserrat:wght@600;700;800&family=Oswald:wght@600&display=swap">
<style>
:root{
  --white:#ffffff;
  --orange:#f37122;
  --blue:#33a6d7;
  --green:#acd037;
  --ink:#1d1d1b;
  --text:#333333;
  --stage:#959595;
  --diagram-blue:#3f86c4;
  --diagram-orange:#e8873a;
  --diagram-gray:#c9c9c9;
}
*{box-sizing:border-box;margin:0;padding:0}
html,body{width:1200px;height:1200px;overflow:hidden;background:var(--stage)}
.spread{position:absolute;left:19px;top:207px;width:1235px;height:836px;transform:scale(0.94);transform-origin:0 0}
.page{position:absolute;top:0;width:596px;height:836px;background:var(--white);overflow:hidden;font-family:"Didact Gothic",sans-serif;color:var(--text)}
.page--front{left:0}
.page--back{left:639px}
.abs{position:absolute}

/* photo areas */
.photo-sky{left:0;top:0;width:596px;height:230px;background:linear-gradient(180deg,#a9c6e2 0%,#e9eef3 38%,#dfe6ec 55%,#7f96a8 72%,#5f7f78 86%,#4d7452 100%)}
.photo-forest{left:0;top:0;width:596px;height:190px;background:linear-gradient(90deg,#2a2116 0%,#4a3a22 25%,#3c3a1c 45%,#6b7a4a 50%,#3b3320 56%,#4a3a22 78%,#261d13 100%)}
.photo-portrait{left:357px;top:80px;width:214px;height:214px;border-radius:50%;border:6px solid var(--white);background:radial-gradient(circle at 50% 40%,#d9c3b0 0%,#a98a76 40%,#6e3a36 75%,#4a2a2a 100%)}

/* brand */
.brand{display:flex;align-items:center;gap:8px}
.brand__dot{width:30px;height:30px;border-radius:50%;background:var(--orange)}
.brand__name{font-family:"Didact Gothic",sans-serif;color:var(--blue);line-height:1}
.brand--front{left:20px;top:28px}
.brand--front .brand__dot{width:60px;height:60px}
.brand--front .brand__name{font-size:31px}
.brand--back{left:398px;top:728px}
.brand--back .brand__name{font-size:18px}

/* bands */
.band-orange{left:0;width:596px;background:var(--orange)}
.panel-blue{left:333px;width:255px;background:var(--blue);border-radius:14px;color:var(--white)}

/* front title block */
.title-top{left:20px;top:230px;font-family:"Oswald",sans-serif;font-weight:600;font-size:31px;color:var(--ink);letter-spacing:-.5px;line-height:1}
.title-main{left:20px;top:262px;font-family:"Montserrat",sans-serif;font-weight:800;font-size:38px;color:var(--white);letter-spacing:1px;line-height:1}
.pill-green{left:0;background:var(--green);color:var(--white);font-family:"Montserrat",sans-serif;font-weight:600;border-radius:0 20px 20px 0;padding:0 0 0 20px;display:flex;align-items:center}
.pill-session{top:310px;width:280px;height:37px;font-size:19px}
.pill-facilitator{top:642px;width:325px;height:30px;font-size:17px}
.date{left:20px;top:360px;font-family:"Montserrat",sans-serif;font-weight:800;font-size:17px;line-height:21px;color:var(--white)}

.heading{font-family:"Montserrat",sans-serif;font-weight:600;color:var(--orange);line-height:1}
.body{font-size:12.6px;line-height:15.3px;text-align:justify}
.sec-info-h{left:19px;top:418px;font-size:19px}
.sec-info-p{left:19px;top:441px;width:302px}
.sec-who-h{left:19px;top:516px;font-size:19px}
.sec-who-p{left:19px;top:539px;width:302px}
.link{left:20px;top:676px;font-size:15px;color:var(--ink)}
.sec-book-h{left:20px;top:708px;font-size:19px}
.sec-book-p{left:20px;top:732px;font-family:"Montserrat",sans-serif;font-weight:600;font-size:12px;line-height:15px;color:var(--ink)}

.facilitator{left:333px;top:300px;width:255px;text-align:center;font-family:"Montserrat",sans-serif;font-weight:600;line-height:20px}
.facilitator__label{font-size:18px;margin-bottom:2px}
.facilitator__name{font-size:15.5px}
.facilitator-bio{left:343px;top:393px;width:235px;font-size:14.3px;line-height:16.3px;text-align:justify;color:var(--white)}

/* footer */
.footer{left:0;top:778px;width:596px;height:48px;background:var(--blue)}
.footer__contact{top:795px;font-size:9.5px;color:var(--white);line-height:11px}
.footer__contact b{font-family:"Montserrat",sans-serif;font-weight:600}
.footer__contact small{font-size:7.5px;display:block}
.footer__email{left:20px}
.footer__tel{left:195px;top:795px}
.footer__venue-bg{left:340px;top:775px;width:262px;height:54px;background:var(--orange);border:4px solid var(--white);border-radius:30px 0 0 30px}
.footer__venue{left:373px;top:789px;font-size:9.5px;line-height:12px;color:var(--ink)}
.footer__venue b{font-family:"Montserrat",sans-serif;font-weight:700}

/* back page */
.back-title{left:20px;top:188px;font-family:"Montserrat",sans-serif;font-weight:800;font-size:18.5px;line-height:23px;color:var(--ink)}
.back-what{left:20px;top:236px;width:296px;font-size:11px;line-height:14px;text-align:justify;color:var(--white)}
.back-program-h{left:20px;top:352px;font-size:19px}
.back-program-p{left:20px;top:378px;width:296px;font-size:10.6px;line-height:12.8px;text-align:justify;color:var(--ink)}
.back-program-p p+p{margin-top:5px}
.cycle{left:0;top:470px;width:336px;height:250px}
.quote{left:28px;top:724px;font-family:"Berkshire Swash",serif;font-size:31px;color:var(--green)}

.why{left:345px;top:145px;width:233px;font-size:11px;line-height:14px}
.why h3{font-family:"Montserrat",sans-serif;font-weight:700;font-size:18px;line-height:22px;margin-bottom:5px}
.why p{text-align:justify}
.why .lead{font-family:"Montserrat",sans-serif;font-weight:700;font-size:10.3px;line-height:13.5px;margin-top:6px;text-align:left}
.why ol{list-style:none;margin-top:6px}
.why li{position:relative;padding-left:15px;margin-bottom:6px}
.why li::before{content:attr(data-n);position:absolute;left:0;top:1px;width:11px;height:11px;border-radius:50%;background:var(--white);color:var(--blue);font-family:"Montserrat",sans-serif;font-weight:800;font-size:8px;line-height:11px;text-align:center}
.why h3.how{margin-top:8px;margin-bottom:2px}
</style>
</head>
<body>
<div class="spread">

  <!-- Front page -->
  <section class="page page--front">
    <div class="abs photo-sky" role="img" aria-label="Photo of a wide sky with clouds above distant mountains"></div>
    <div class="abs brand brand--front"><span class="brand__dot"></span><span class="brand__name">bright<br>meadow</span></div>

    <div class="abs band-orange" style="top:220px;height:186px"></div>
    <div class="abs title-top">QUIET VENTURE</div>
    <div class="abs title-main">PATHWAY</div>
    <div class="abs pill-green pill-session">INFORMATION SESSION</div>
    <div class="abs date">THURSDAY 18TH JULY 2019,<br>FROM 19:30 TO 21:00</div>

    <h2 class="abs heading sec-info-h">INFORMATION SESSION:</h2>
    <p class="abs body sec-info-p">The purpose of this Information Session is to give you a real insight into the Quiet Venture Pathway and how it can help you get the most out of your work and life.</p>

    <h2 class="abs heading sec-who-h">WHO CAN COME?</h2>
    <p class="abs body sec-who-p">The Information Session is free and whether you come on your own, or with friends or family, you'll be warmly welcome. It will take place on Thursday the 23rd July 2019, from 19:30 to 21:00, at Lumen Coworking. Please get in touch for more info or to book a place.</p>

    <div class="abs pill-green pill-facilitator">MORE ABOUT THE FACILITATOR:</div>
    <p class="abs link">www.adrianvelmor.com</p>

    <h2 class="abs heading sec-book-h">INFORMATION &amp; BOOKING:</h2>
    <p class="abs sec-book-p">Please contact for more information or to<br>book a place</p>

    <div class="abs panel-blue" style="top:150px;height:610px"></div>
    <div class="abs photo-portrait" role="img" aria-label="Portrait photo of the facilitator"></div>
    <div class="abs facilitator">
      <div class="facilitator__label">FACILITATOR:</div>
      <div class="facilitator__name">Dr Adrian Velmor, Visiting<br>Research Fellow, Harwick<br>University</div>
    </div>
    <p class="abs facilitator-bio">Adrian joined Harwick University (School of Management) as a Lecturer in Entrepreneurship in 2015. He completed his PhD in Entrepreneurship at Northgate Business School (University of Northgate) in 2014. His dissertation received the Lindqvist Doctoral Dissertation Award from the Society for Enterprise Studies. Adrian began his working career in the semiconductor industry as a production engineer (Voltrane), and then in healthcare as a sales engineer (Kestrel Systems). After his MBA, he worked as a strategy consultant at Tagus Business School. Originally from Portugal, Adrian enjoys designing and launching new ideas, international communities, mindfulness retreats, and musical improvisation.</p>

    <div class="abs footer"></div>
    <p class="abs footer__contact footer__email"><b>Email:</b> info@brightmeadow.io</p>
    <p class="abs footer__contact footer__tel"><b>Tel:</b> +34 611 402 739<small>(video call and messaging)</small></p>
    <div class="abs footer__venue-bg"></div>
    <p class="abs footer__venue"><b>Venue:</b><br>Lumen Coworking, C/ Verdaguer 41, Barcelona</p>
  </section>

  <!-- Back page -->
  <section class="page page--back">
    <div class="abs photo-forest" role="img" aria-label="Photo of a person walking along a path through a pine forest"></div>
    <div class="abs band-orange" style="top:180px;height:162px"></div>
    <h2 class="abs back-title">WHAT IS QUIET<br>VENTURE</h2>
    <p class="abs back-what">Being mindful means being aware and awake. Entrepreneurship is the creation of a new form of organising. Quiet Venture is then the process of creating or redesigning your work and life with awareness, in a way that is reflective of you, of your passions and values, thus conducing to a greater sense of fulfilment and happiness.</p>

    <h2 class="abs heading back-program-h">THE PROGRAM</h2>
    <div class="abs back-program-p">
      <p>The Quiet Venture Pathway is a 4-month long transformative journey for people who feel stuck or not entirely satisfied with their work and/or life. It will be of benefit for everyone, at any stage.<br>The Program consists of a series of four</p>
      <p>5-hour workshops, one per month, complemented by 2-hour weekly peer support meetings. It combines mindfulness techniques, design thinking methodology and entrepreneurship frameworks to achieve the desired outcomes.</p>
    </div>

    <svg class="abs cycle" viewBox="0 0 336 250" role="img" aria-label="Cycle of four workshops joined by weekly peer support meetings">
      <g font-family="Didact Gothic, sans-serif" text-anchor="middle">
        <g stroke-width="5" fill="none" stroke-linecap="round">
          <path d="M198 108 L212 122" stroke="var(--green)"/>
          <path d="M212 185 L200 197" stroke="var(--diagram-blue)"/>
          <path d="M128 212 L114 200" stroke="var(--diagram-orange)"/>
          <path d="M112 106 L126 94" stroke="var(--diagram-gray)"/>
        </g>
        <path d="M206 127 L220 130 L217 116 Z" fill="var(--green)"/>
        <path d="M206 190 L194 203 L208 204 Z" fill="var(--diagram-blue)"/>
        <path d="M121 195 L108 192 L111 206 Z" fill="var(--diagram-orange)"/>
        <path d="M119 90 L132 89 L130 102 Z" fill="var(--diagram-gray)"/>

        <circle cx="163" cy="85" r="36" fill="var(--green)"/>
        <circle cx="240" cy="147" r="36" fill="var(--diagram-blue)"/>
        <circle cx="163" cy="210" r="36" fill="var(--diagram-orange)"/>
        <circle cx="86" cy="147" r="36" fill="var(--diagram-gray)"/>

        <g fill="#fff" font-size="7.5">
          <text x="163" y="76">Workshop 1</text><text x="163" y="88" font-size="9">-INSIGHT-</text><text x="163" y="98" font-size="6.5">(5 hours)</text>
          <text x="240" y="138">Workshop 2</text><text x="240" y="150" font-size="9">-DESIGN-</text><text x="240" y="160" font-size="6.5">(5 hours)</text>
          <text x="163" y="201">Workshop 3</text><text x="163" y="213" font-size="9">-EXECUTE-</text><text x="163" y="223" font-size="6.5">(5 hours)</text>
          <text x="86" y="138">Workshop 4</text><text x="86" y="150" font-size="9">-PRESENT-</text><text x="86" y="160" font-size="6.5">(5 hours)</text>
        </g>
        <g fill="#777" font-size="7" font-style="italic">
          <text x="88" y="97">WPS meetings</text>
          <text x="241" y="94">Weekly Peer Support</text><text x="241" y="103">(WPS) meetings</text>
          <text x="88" y="208">WPS meetings</text>
          <text x="238" y="208">WPS meetings</text>
        </g>
      </g>
    </svg>

    <p class="abs quote">“The Way Out is In”</p>
    <div class="abs brand brand--back"><span class="brand__dot"></span><span class="brand__name">bright<br>meadow</span></div>

    <div class="abs panel-blue" style="top:130px;height:588px"></div>
    <div class="abs why">
      <h3>WHY</h3>
      <p>Many people are not entirely satisfied with their work, but they don't know what to do about it. The Quiet Venture Pathway offers an opportunity, a safe place, a collective journey to help you reflect, design, and (very likely) do something about it.</p>
      <p class="lead">By the end of the Program, you should have:</p>
      <ol>
        <li data-n="1">Increased awareness, clarity and confidence</li>
        <li data-n="2">A deeper insight on what makes you happier and what you want</li>
        <li data-n="3">A clear design integrating your intended work and life</li>
        <li data-n="4">Initiated the execution of this design.</li>
      </ol>
      <h3 class="how">How</h3>
      <p class="lead" style="margin-top:0">This Program differs from existing entrepreneurial programs in many ways:</p>
      <ol>
        <li data-n="1">It starts upstream with mindfulness and self analysis to look deeply into yourself</li>
        <li data-n="2">Design and execution decisions are rooted on happiness rather than (only) financials</li>
        <li data-n="3">The process is holistic and inclusive, aiming at designing an integrated work and life, and on building synergies between your different parts.</li>
      </ol>
      <p>The Program format includes lectures, individual work, group sharing, guided activities, experiential exercises, video, audio, handouts and other resources.</p>
    </div>

    <div class="abs footer"></div>
    <p class="abs footer__contact footer__email"><b>Email:</b> info@brightmeadow.io</p>
    <p class="abs footer__contact footer__tel"><b>Tel:</b> +34 611 402 739<small>(video call and messaging)</small></p>
    <div class="abs footer__venue-bg"></div>
    <p class="abs footer__venue"><b>Venue:</b><br>Lumen Coworking, C/ Verdaguer 41, Barcelona</p>
  </section>

</div>
</body>
</html>
```